Letterhead design for Sleep Consulting Business

I'm looking for a new letterhead (heading/footer) design for my Sleep Consulting Business, I work with families to help their children improve their sleep.

The heading/footer will used in Microsoft Word Only-to be used for all of my documents such as writing Sleep Plans. I need to utilize as much working space in the document as possible. This will NOT be printed out on paper- it will only be used for heading/footer on microsoft word, then emailed to clients, who may print it at home.

My brand colors:
Dark Blue Hex: 1F2A42
Lighter Blueish Hex: 90BEC9
You're welcome to check out my website for inspiration- it is freshly created with other colors as well, and I love the outcome. www.quietharborsleep.example

Target Market(s)

Tired parents

Font styles to use
Script
Other font styles liked:
• Great Vibe, Lato or Just Another Hand are all used currently for my brand. Open to other options.

Requirements
Must have
• The letterhead (heading/footer) MUST be kept narrow (height-wise), so I have plenty of space on my document, while including important information.

It should look professional on screen, and when printed.

Must include my business name OR logo (Quiet Harbor Sleep Consulting), and my email address. Tessa@quietharborsleep.example

Website is optional, not required, just if you need to fill in a spot: www.quietharborsleep.example

```html
<!DOCTYPE html>
<html lang="en">
<head>
<meta charset="utf-8">
<title>Quiet Harbor Sleep Consulting – Letterhead</title>
<link rel="stylesheet" href="https://fonts.googleapis.com/css2?family=Arimo:wght@400&family=Lato:wght@400&display=swap">
<style>
  :root {
    --navy: #1F2A42;
    --sky: #90BEC9;
    --backdrop: #e9e7e4;
    --paper: #f6f6f7;
    --ink: #505257;
    --mark-faint: #e6eaee;
    --signature-tone: #d9dbe0;
  }
  * { margin: 0; padding: 0; box-sizing: border-box; }
  html, body {
    width: 1200px; height: 1141px; overflow: hidden;
    background: var(--backdrop);
  }
  .page {
    position: absolute; left: 216px; top: 30px;
    width: 768px; height: 1081px;
    background: var(--paper);
    box-shadow: 0 2px 8px rgba(0,0,0,0.18);
    overflow: hidden;
    font-family: "Arimo", Arial, sans-serif;
    color: var(--ink);
  }
  .backdrop-mark {
    position: absolute; left: 164px; top: 331px;
    width: 402px; height: 402px; border-radius: 50%;
    background: var(--mark-faint);
  }
  .brand {
    position: absolute; left: 209px; top: 83px;
    display: flex; align-items: center; gap: 22px;
  }
  .brand-dot {
    width: 84px; height: 84px; border-radius: 50%;
    background: var(--navy);
  }
  .brand-name {
    font-family: "Lato", Arial, sans-serif; font-weight: 400;
    font-size: 27px; line-height: 1.2; color: var(--navy);
  }
  .salutation {
    position: absolute; left: 57px; top: 268px;
    font-size: 20px; color: var(--ink);
  }
  .letter-body {
    position: absolute; left: 57px; top: 328px; width: 656px;
    font-size: 11px; line-height: 16.5px; text-align: justify;
  }
  .letter-body p { margin-bottom: 16px; }
  .closing {
    position: absolute; left: 57px; top: 689px; font-size: 11px;
  }
  .signature {
    position: absolute; left: 52px; top: 724px;
    width: 222px; height: 64px; background: var(--signature-tone);
    border-radius: 3px;
  }
  .ornament {
    position: absolute; left: 346px; width: 76px;
    background: var(--navy); border-radius: 10px; opacity: 0.85;
  }
  .ornament-top { top: 971px; height: 17px; }
  .ornament-bottom { top: 1036px; height: 19px; }
  .contact-band {
    position: absolute; left: 45px; top: 998px;
    width: 683px; height: 33px; background: var(--navy);
    color: #ffffff; font-size: 12px; letter-spacing: 0.2px;
    display: flex; align-items: center; justify-content: center;
    text-transform: uppercase;
  }
</style>
</head>
<body>
  <main class="page">
    <div class="backdrop-mark"></div>

    <header class="brand">
      <div class="brand-dot"></div>
      <div class="brand-name">Quiet Harbor<br>Sleep Consulting</div>
    </header>

    <p class="salutation">Dear Mr. Smith,</p>

    <section class="letter-body">
      <p>Lorem ipsum dolor sit amet, consectetur adipiscing elit. Donec orci purus, luctus vitae dignissim eu, iaculis sed purus. Vivamus faucibus, ipsum nec aliquet viverra, leo mauris condimentum ligula, sit amet sagittis enim ligula quis arcu. Nam egestas tortor id nisi porttitor mattis. In tortor ante, ultricies in suscipit a, tempus non massa. Vivamus et auctor mi. Fusce vel massa nulla. Phasellus nec eros mauris, et scelerisque orci.</p>
      <p>Donec malesuada orci vitae nulla accumsan porta a id massa. Quisque accumsan iaculis magna sit amet fringilla. Maecenas consequat, magna eget tincidunt semper, odio nibh rutrum mi, id feugiat ante nisi eu risus. Vestibulum nunc orci, rhoncus a placerat in, ultricies in mi. Cras mattis varius eros, vel fringilla nisi suscipit eget. Quisque scelerisque sagittis nulla at porttitor.</p>
      <p>Sed id augue vitae urna euismod commodo aliquet a quam. Pellentesque arcu velit, cursus et malesuada ut, consequat et diam. Nullam erat sem, rhoncus id ullamcorper vitae, rhoncus et arcu. In ultricies ultricies nulla, ut rutrum nisi iaculis at. Donec eu magna a metus ornare faucibus. Fusce aliquet faucibus ultricies. Morbi semper, est id tincidunt gravida, sem arcu adipiscing lacus, ac bibendum nulla leo eu purus. Quisque nec diam sed risus consectetur a ccumsan quis quis nibh. Vestibulum id purus lorem.</p>
      <p>It is a long established fact that a reader will be distracted by the readable content of a page when looking at its layout. The point of using Lorem Ipsum is that it has a more-or-less normal distribution of letters, as opposed to using 'Content here, content here', making it look like readable English. Many desktop publishing packages</p>
      <p>ada ut, consequat et diam. Nullam erat sem, rhoncus id ullamcorper vitae, rhoncus et arcu. In ultricies ultricies nulla, ut rutrum nisi iaculis at. Donec eu magna a metus ornare faucibus. Fusce aliquet faucibus ultricies. Morbi semper,</p>
    </section>

    <p class="closing">Sincerely,</p>
    <div class="signature" role="img" aria-label="Handwritten signature of the sender"></div>

    <footer>
      <div class="ornament ornament-top" role="img" aria-label="Decorative scroll flourish"></div>
      <div class="contact-band">Tessa@quietharborsleep.example | www.quietharborsleep.example</div>
      <div class="ornament ornament-bottom" role="img" aria-label="Decorative scroll flourish"></div>
    </footer>
  </main>
</body>
</html>
```